Frostvel.io - Polar Expeditions Specialists

We need a modern, visually striking business card for Frostvel.io, a company specialized in selling expedition cruises to the most remote regions on Earth, with a focus on the Arctic and Antarctica. The design should instantly communicate that the cardholder is an expert in polar travel. Use clean, premium aesthetics with cool tones like icy blue and white, possibly incorporating polar imagery (ice, glaciers, penguins, etc.)

Contact Information for Business Card

Feels high-end and trustworthy.. Visually memorable — encourages people to keep it

Colors
0054AA
0677BA
7BADD7
CADEEF
E8F1F8

Requirements
Must have
• ice, glaciers, penguins, montains
Nice to have
• modern, transparente,

```html
<!DOCTYPE html>
<html lang="en">
<head>
<meta charset="utf-8">
<title>Frostvel.io Business Card</title>
<link href="https://fonts.googleapis.com/css2?family=Poppins:wght@400;600;700&family=Montserrat:wght@400&display=swap" rel="stylesheet">
<style>
  :root {
    --bg: #d3d3d3;
    --paper: #f1f1ef;
    --brand-blue: #2f74c0;
    --edge-blue: #2b6fbd;
    --text-grey: #6f6f6f;
    --divider: #dcdcd9;
  }
  * { margin: 0; padding: 0; box-sizing: border-box; }
  html, body { width: 1200px; height: 1051px; overflow: hidden; }
  body {
    background: var(--bg);
    font-family: "Poppins", sans-serif;
    position: relative;
  }
  .card {
    position: absolute;
    left: 320px;
    width: 560px;
    height: 320px;
    background: var(--paper);
    border-bottom: 4px solid var(--edge-blue);
    box-shadow: 0 12px 30px rgba(0,0,0,0.18);
  }
  .card--front { top: 150px; }
  .card--back { top: 560px; display: flex; align-items: center; }

  .brand { display: flex; flex-direction: column; align-items: flex-start; }
  .brand__row { display: flex; align-items: center; gap: 12px; }
  .brand__dot { border-radius: 50%; background: var(--brand-blue); }
  .brand__name { color: var(--brand-blue); font-weight: 700; line-height: 1; }
  .brand__tagline { color: var(--brand-blue); font-weight: 400; letter-spacing: 0.02em; }

  .card--front .brand { position: absolute; left: 130px; top: 118px; }
  .card--front .brand__dot { width: 26px; height: 26px; }
  .card--front .brand__name { font-size: 52px; }
  .card--front .brand__tagline { font-size: 13px; margin: 6px 0 0 38px; }

  .card--back .brand { width: 270px; padding-left: 44px; }
  .card--back .brand__dot { width: 16px; height: 16px; }
  .card--back .brand__name { font-size: 33px; }
  .card--back .brand__tagline { font-size: 8.5px; margin: 4px 0 0 28px; }

  .divider { width: 1px; height: 150px; background: var(--divider); box-shadow: 1px 0 0 #fff; }

  .contact { padding-left: 26px; }
  .contact__name { color: var(--brand-blue); font-weight: 700; font-size: 18px; letter-spacing: 0.01em; }
  .contact__role { color: var(--text-grey); font-size: 13px; margin-bottom: 14px; }
  .contact__list { list-style: none; font-family: "Montserrat", sans-serif; font-size: 12.5px; color: var(--text-grey); }
  .contact__list li { display: flex; align-items: center; gap: 8px; margin-bottom: 5px; }
  .contact__icon { width: 11px; height: 11px; fill: var(--brand-blue); flex: none; }
</style>
</head>
<body>
  <section class="card card--front">
    <div class="brand">
      <div class="brand__row">
        <span class="brand__dot"></span>
        <span class="brand__name">Frostvel.io</span>
      </div>
      <span class="brand__tagline">Polar Expeditions Specialists</span>
    </div>
  </section>

  <section class="card card--back">
    <div class="brand">
      <div class="brand__row">
        <span class="brand__dot"></span>
        <span class="brand__name">Frostvel.io</span>
      </div>
      <span class="brand__tagline">Polar Expeditions Specialists</span>
    </div>
    <div class="divider"></div>
    <div class="contact">
      <p class="contact__name">MARCUS LINDQVIST</p>
      <p class="contact__role">President</p>
      <ul class="contact__list">
        <li>
          <svg class="contact__icon" viewBox="0 0 24 24"><path d="M6.6 10.8a15.1 15.1 0 0 0 6.6 6.6l2.2-2.2a1 1 0 0 1 1-.25 11.4 11.4 0 0 0 3.6.57 1 1 0 0 1 1 1V20a1 1 0 0 1-1 1A17 17 0 0 1 3 4a1 1 0 0 1 1-1h3.5a1 1 0 0 1 1 1c0 1.25.2 2.45.57 3.57a1 1 0 0 1-.25 1z"/></svg>
          555-318-4072
        </li>
        <li>
          <svg class="contact__icon" viewBox="0 0 24 24"><path d="M2 5h20v14H2z M2 5l10 8 10-8" fill="none" stroke="#2f74c0" stroke-width="0"/><path d="M2 5h20v2l-10 7L2 7z M2 9l10 7 10-7v10H2z"/></svg>
          marcus@frostvel.io
        </li>
        <li>
          <svg class="contact__icon" viewBox="0 0 24 24"><circle cx="12" cy="12" r="10"/></svg>
          www.frostvel.io
        </li>
      </ul>
    </div>
  </section>
</body>
</html>
```